Design a website for our summer bar "Velmo"

Dear designers,

We are seeking a creative and talented individual or team to design a website for our summer bar "Velmo". We would like to have an attractive and user-friendly website that perfectly captures the ambiance of our bar.

On the website, we would like to include the following elements:

Photos: Use photos from our Instagram and Facebook pages + see attachment. (@Dunelamp48Vel) to showcase the visual appeal of our bar.
Menu: Ensure that the menu is clear and easy to read, with attractive images of our food and drinks.
Opening hours: Mention the opening hours of our summer bar, so visitors know when they can pay us a visit.
Quotes: Include some inspiring and fun quotes that reflect the relaxed and vibrant atmosphere of our bar.
Important: We want the website to be developed in a WordPress environment so that we can make changes ourselves if needed. Make sure the design is fully prepared for implementation in WordPress.
Extra; Moving objects, we want a site that lives, not just a plain site with no movement, no excitement. We love some action and effects!
Here are some key points to keep in mind while designing:

Create a summery and cheerful look and feel that aligns with the atmosphere of our bar.
Use our branding, which can be found on our Instagram and Facebook pages (@Dunelamp48Vel), as the basis for the color scheme and overall appearance of the website.

Make the website responsive, ensuring it displays well on both desktop and mobile devices.
We are looking forward to seeing your creative proposals! Feel free to reach out if you need any additional information.

Coding

Coded - Design and coding required

Number of Pages Required

1 page

Requirements
Nice to have
• In attachment is a video from the opening. would be nice if this is included in the website. (if it fits the design).

```html
<!DOCTYPE html>
<html lang="en">
<head>
<meta charset="utf-8">
<title>Velmo – Summer Bar</title>
<link rel="stylesheet" href="https://fonts.googleapis.com/css2?family=Roboto:ital,wght@0,400;0,500;0,700;0,900;1,700;1,900&display=swap">
<style>
:root{
  --red:#d0161f;
  --navy:#2e2f63;
  --blue:#1f80c8;
  --ink:#1d1d1d;
  --text:#444;
  --footer:#1b1b1b;
  --white:#fff;
}
*{box-sizing:border-box;margin:0;padding:0}
html,body{width:1200px;height:3852px;overflow:hidden}
body{position:relative;font-family:'Roboto',sans-serif;color:var(--text);background:var(--white)}
.abs{position:absolute}
.section-title{position:absolute;left:0;width:1200px;text-align:center;font:italic 900 35px 'Roboto',sans-serif;letter-spacing:-.5px;color:var(--ink);text-transform:uppercase}
.section-title::after{content:"";display:block;width:60px;height:4px;background:var(--red);margin:14px auto 0}
.btn{position:absolute;display:flex;align-items:center;justify-content:center;gap:8px;background:var(--red);color:#fff;font:700 13px 'Roboto',sans-serif;text-transform:uppercase;border-radius:3px}
.btn svg{width:13px;height:13px}
.photo{position:absolute}

/* header */
.brand{position:absolute;left:118px;top:30px;display:flex;align-items:center;gap:10px;font:700 48px 'Roboto',sans-serif;color:var(--navy)}
.brand i{display:block;width:22px;height:22px;background:var(--red)}
.topbar{position:absolute;left:505px;top:18px;display:flex;gap:30px;font:500 15px 'Roboto',sans-serif;color:var(--ink)}
.topbar span{display:flex;align-items:center;gap:12px}
.ico{width:32px;height:32px;border-radius:50%;background:var(--red);display:flex;align-items:center;justify-content:center}
.ico svg{width:15px;height:15px}
.rule{position:absolute;left:396px;top:65px;width:694px;height:2px;background:var(--red)}
.nav{position:absolute;left:396px;top:80px;width:694px;display:flex;justify-content:space-between;font:400 15px 'Roboto',sans-serif;color:#333;text-transform:uppercase;padding:0 8px}
.nav .on{color:var(--red);font-weight:500}

/* hero */
.hero{position:absolute;left:0;top:116px;width:1200px;height:628px;background:linear-gradient(180deg,#c9a27a 0%,#7d5a3a 35%,#3c2c22 70%,#4a4440 100%)}
.hero h1{position:absolute;top:310px;width:1200px;text-align:center;font:italic 900 54px 'Roboto',sans-serif;color:#fff;text-transform:uppercase}
.hero p{position:absolute;top:386px;width:1200px;text-align:center;font:500 15px/24px 'Roboto',sans-serif;color:#fff}

/* about */
.about-title{position:absolute;left:112px;top:842px;font:italic 900 35px 'Roboto',sans-serif;color:var(--ink);text-transform:uppercase}
.about-title::after{content:"";display:block;width:60px;height:4px;background:var(--red);margin-top:10px}
.about-text{position:absolute;left:112px;top:918px;width:462px;font:400 14px/24px 'Roboto',sans-serif;text-align:justify;color:#444}

/* bar menu */
.band-red{position:absolute;left:0;top:1405px;width:1200px;height:367px;background:var(--red)}
.menu-box{position:absolute;left:112px;top:1320px;width:976px;height:498px;background:var(--navy)}
.menu-box .section-title{width:976px;top:60px;color:#fff}
.dish{position:absolute;border-radius:50%;border:3px solid #fff}
.dish.big{border-color:var(--red)}
.dish-label{position:absolute;width:200px;text-align:center;font:700 15px 'Roboto',sans-serif;color:#fff}

/* restaurant menus */
.card{position:absolute;top:1988px;width:313px;height:432px;background:#fff;box-shadow:0 4px 22px rgba(0,0,0,.12);text-align:center}
.card.active{border:1px solid var(--red)}
.card .photo{left:0;top:0;width:100%;height:219px}
.card h3{position:absolute;top:262px;width:100%;font:500 19px 'Roboto',sans-serif;color:var(--ink)}
.card h3::after{content:"";display:block;width:40px;height:2px;background:#e89a35;margin:14px auto 0}
.card p{position:absolute;top:326px;left:22px;right:22px;font:400 14px/22px 'Roboto',sans-serif;color:#555}

/* quotes */
.quotes{position:absolute;left:0;top:2506px;width:1200px;height:316px;background:var(--blue)}
.quotes .section-title{top:56px;color:#fff}
.quotes blockquote{position:absolute;top:150px;left:170px;width:860px;text-align:center;font:italic 700 19px/31px 'Roboto',sans-serif;color:#fff}
.qmark{position:absolute;width:40px;height:32px}

/* events */
.event{position:absolute;left:585px;width:510px;height:92px}
.date{position:absolute;left:0;top:0;width:90px;height:92px;border:2px solid var(--navy);border-radius:10px;overflow:hidden;background:#fff;text-align:center}
.date b{display:block;background:var(--navy);color:#fff;font:500 17px/34px 'Roboto',sans-serif}
.date span{display:block;font:500 38px/54px 'Roboto',sans-serif;color:var(--navy)}
.event h4{position:absolute;left:125px;top:2px;font:500 14px 'Roboto',sans-serif;color:#222;text-transform:uppercase}
.meta{position:absolute;left:125px;top:28px;display:flex;align-items:center;gap:10px;font:700 13px 'Roboto',sans-serif;color:#222}
.meta svg{width:13px;height:13px}
.event p{position:absolute;left:125px;top:54px;width:385px;font:400 13px/17px 'Roboto',sans-serif;color:#555}

/* footer */
.footer{position:absolute;left:0;top:3435px;width:1200px;height:417px;background:var(--footer);color:#fff}
.footer .brand{left:115px;top:90px;color:#fff}
.fcol{position:absolute;top:58px}
.fcol h5{font:700 16px 'Roboto',sans-serif;text-transform:uppercase;margin-bottom:16px}
.fcol li{list-style:none;display:flex;gap:18px;font:400 15px/34px 'Roboto',sans-serif}
.fcol li svg{width:10px;height:10px;margin-top:12px}
.contact-item{display:flex;gap:14px;margin-bottom:12px}
.contact-item svg{width:13px;height:13px;margin-top:3px;flex:none}
.contact-item small{display:block;font:700 11px 'Roboto',sans-serif}
.contact-item span{font:400 15px/20px 'Roboto',sans-serif}
.frule{position:absolute;left:112px;top:345px;width:976px;height:1px;background:#444}
.copy{position:absolute;top:372px;width:1200px;text-align:center;font:400 14px 'Roboto',sans-serif}
</style>
</head>
<body>

<svg width="0" height="0" style="position:absolute">
  <defs>
    <symbol id="chev" viewBox="0 0 10 10"><path d="M1 1l3 4-3 4M5 1l3 4-3 4" fill="none" stroke="currentColor" stroke-width="1.5"/></symbol>
    <symbol id="arrow-c" viewBox="0 0 14 14"><circle cx="7" cy="7" r="7" fill="#fff"/><path d="M5.5 4l3 3-3 3" fill="none" stroke="#d0161f" stroke-width="2"/></symbol>
    <symbol id="pin" viewBox="0 0 12 14"><path d="M6 0a5 5 0 0 1 5 5c0 4-5 9-5 9S1 9 1 5a5 5 0 0 1 5-5z" fill="currentColor"/><circle cx="6" cy="5" r="2" fill="#fff"/></symbol>
    <symbol id="user" viewBox="0 0 12 12"><circle cx="6" cy="3.2" r="3" fill="currentColor"/><path d="M0 12c0-4 3-5 6-5s6 1 6 5z" fill="currentColor"/></symbol>
    <symbol id="phone" viewBox="0 0 14 14"><path d="M3 0l3 3-2 2c1 2 3 4 5 5l2-2 3 3-2 3C6 14 0 8 0 2z" fill="currentColor"/></symbol>
    <symbol id="mail" viewBox="0 0 14 11"><rect x="0.5" y="0.5" width="13" height="10" rx="1" fill="none" stroke="currentColor" stroke-width="1.4"/><path d="M1 1l6 5 6-5" fill="none" stroke="currentColor" stroke-width="1.4"/></symbol>
    <symbol id="clock" viewBox="0 0 14 14"><circle cx="7" cy="7" r="6" fill="none" stroke="currentColor" stroke-width="1.6"/><path d="M7 3.5V7h3" fill="none" stroke="currentColor" stroke-width="1.6"/></symbol>
  </defs>
</svg>

<!-- Header -->
<header>
  <div class="brand"><i></i>Velmo</div>
  <div class="topbar">
    <span><span class="ico" style="color:#fff"><svg><use href="#clock"/></svg></span>Mon&nbsp; 9.00am - 7.00pm</span>
    <span><span class="ico" style="color:#fff"><svg><use href="#mail"/></svg></span>info@velmo.com</span>
    <span><span class="ico" style="color:#fff"><svg><use href="#phone"/></svg></span>+1 555 010 2040</span>
  </div>
  <div class="rule"></div>
  <nav class="nav">
    <span class="on">Home</span><span>|</span><span>About Us</span><span>|</span><span>Bar</span><span>|</span><span>Restaurant-Menus</span><span>|</span><span>Event</span><span>|</span><span>Contact Us</span>
  </nav>
</header>

<!-- Hero -->
<section class="hero" role="img" aria-label="Evening view of the open-air bar terrace under large canvas sails with tables and barrel tables">
  <h1>Welcome to&nbsp; Velmo</h1>
  <p>Lorem ipsum dolor sit amet, consectetur adipiscing elit, sed do eiusmod tempor<br>incididunt ut labore et dolore magna aliquat enim ad minim veniamnostrud.</p>
  <div class="btn" style="left:527px;top:464px;width:146px;height:42px">Get Started <svg><use href="#arrow-c"/></svg></div>
</section>

<!-- About -->
<section class="about">
  <h2 class="about-title">About Us</h2>
  <p class="about-text">Lorem ipsum dolor sit amet, consectetur adipiscing elit, sed do eiusmod tempor incididunt ut labore et dolore magna aliqua. Ut enim ad minim veniam, quis nostrud exercitation ullamco laboris nisi ut aliquip ex ea commodo consequat. Duis aute irure dolor in reprehenderit in voluptate velit esse cillum dolore eu fugiat nulla pariatur. Excepteur sint occaecat cupidatat non proident, sunt in culpa qui officia deserunt mollit anim id est laborumLorem ipsum dolor sit amet, consectetur adipiscing elit, sed do eiusmod tempor incididunt ut labore et dolore magna aliqua. Ut enim ad minim veniam, quis nostrud exercitation ullamco laboris nisi ut aliquip ex ea commodo consequat.</p>
  <div class="btn" style="left:112px;top:1178px;width:146px;height:44px">Learn More <svg><use href="#arrow-c"/></svg></div>
  <svg class="abs" style="left:640px;top:840px" width="460" height="390" viewBox="0 0 460 390">
    <polygon points="0,372 10,5 460,5 448,372" fill="var(--red)"/>
    <polygon points="8,375 445,380 445,390 8,385" fill="var(--blue)"/>
  </svg>
  <div class="abs" style="left:628px;top:812px;width:100px;height:160px;background:var(--blue);transform:rotate(6deg)"></div>
  <div class="photo" style="left:662px;top:845px;width:420px;height:365px;background:linear-gradient(135deg,#a46a38,#6b4424 55%,#2c3a44)" role="img" aria-label="Bartender in a dark polo shirt pouring beer from a tap"></div>
</section>

<!-- Bar menu -->
<section>
  <div class="band-red"></div>
  <div class="menu-box">
    <h2 class="section-title">Bar Menu</h2>
    <div class="dish" style="left:15px;top:188px;width:164px;height:164px;background:radial-gradient(circle,#f4a0a0,#d8303a)" role="img" aria-label="Red berry cocktail with ice"></div>
    <div class="dish" style="left:193px;top:188px;width:164px;height:164px;background:radial-gradient(circle,#d8c49a,#5f7a3a)" role="img" aria-label="Drink with dried orange slice and mint"></div>
    <div class="dish big" style="left:377px;top:158px;width:222px;height:222px;background:radial-gradient(circle,#e9b06a,#9a5a3a 60%,#4d8a8a)" role="img" aria-label="Table of mixed snacks and small plates"></div>
    <div class="dish" style="left:619px;top:188px;width:164px;height:164px;background:radial-gradient(circle,#d68e7a,#6b6a6a)" role="img" aria-label="Skewers on a grill"></div>
    <div class="dish" style="left:798px;top:188px;width:164px;height:164px;background:radial-gradient(circle,#f4efe0,#c9a66a)" role="img" aria-label="Glass of frothy white beer"></div>
    <div class="dish-label" style="left:0;top:379px">Lorem ipsum dolor</div>
    <div class="dish-label" style="left:178px;top:379px">Lorem ipsum dolor</div>
    <div class="dish-label" style="left:388px;top:413px">Lorem ipsum dolor</div>
    <div class="dish-label" style="left:603px;top:379px">Lorem ipsum dolor</div>
    <div class="dish-label" style="left:780px;top:379px">Lorem ipsum dolor</div>
  </div>
</section>

<!-- Restaurant menus -->
<section>
  <h2 class="section-title" style="top:1892px">Restaurant Menus</h2>
  <article class="card" style="left:106px">
    <div class="photo" style="background:linear-gradient(160deg,#d8c7a2,#6d5240)" role="img" aria-label="Guests seated at wooden tables in the tent"></div>
    <h3>Lorem ipsum dolor sit</h3>
    <p>Sed ut perspiciatis unde omnis iste natus error sit voluptatem accusan doloremque laudantium, totam rem aperiam</p>
  </article>
  <article class="card active" style="left:443px">
    <div class="photo" style="background:linear-gradient(160deg,#2a3a44,#c9a86a 70%,#e9d8a0)" role="img" aria-label="Beer being poured from a tap into a glass"></div>
    <h3>Lorem ipsum dolor sit</h3>
    <p>Sed ut perspiciatis unde omnis iste natus error sit voluptatem accusan doloremque laudantium, totam rem aperiam</p>
  </article>
  <article class="card" style="left:781px">
    <div class="photo" style="background:linear-gradient(160deg,#3a3e44,#b48a7a 55%,#6a6e74)" role="img" aria-label="Rows of skewers on a grill"></div>
    <h3>Lorem ipsum dolor sit</h3>
    <p>Sed ut perspiciatis unde omnis iste natus error sit voluptatem accusan doloremque laudantium, totam rem aperiam</p>
  </article>
</section>

<!-- Quotes -->
<section class="quotes">
  <h2 class="section-title">Our Quotes</h2>
  <svg class="qmark" style="left:152px;top:130px" viewBox="0 0 40 32"><path d="M2 30V18C2 8 8 3 16 2v6c-4 1-6 4-6 8h6v14zM24 30V18c0-10 6-15 14-16v6c-4 1-6 4-6 8h6v14z" fill="#fff"/></svg>
  <blockquote>Lorem ipsum dolor sit amet consectetur adipiscing elit sed do eiusmod tempor incididunt ut labore et dolore magna&nbsp; enim ad minim veniam quis nostrud exercitation ullamco laboris nisi ut aliquip ex ea commodo consequat. Duis aute irure dolor in reprehenderit.</blockquote>
  <svg class="qmark" style="left:1010px;top:225px" viewBox="0 0 40 32"><path d="M38 2v12c0 10-6 15-14 16v-6c4-1 6-4 6-8h-6V2zM16 2v12c0 10-6 15-14 16v-6c4-1 6-4 6-8H2V2z" fill="#fff"/></svg>
</section>

<!-- Events -->
<section>
  <h2 class="section-title" style="top:2902px">Our Events</h2>
  <div class="photo" style="left:112px;top:2993px;width:424px;height:354px;background:linear-gradient(135deg,#d9b98a,#7a4a26 50%,#2a1a12)" role="img" aria-label="Dark beer being poured into a tulip glass"></div>

  <div class="event" style="top:2993px">
    <div class="date"><b>JUNE</b><span>20</span></div>
    <h4>Lorem ipsum dolor sit amet consectetur</h4>
    <div class="meta"><svg style="color:var(--red)"><use href="#user"/></svg>JOHN DOE <svg style="color:var(--red);margin-left:36px"><use href="#pin"/></svg>Lorem Ipsum Dolor , USA</div>
    <p>Sed ut perspiciatis unde omnis iste natus error sivoluptatem accusantium doloremque laudantium.</p>
  </div>
  <div class="event" style="top:3123px">
    <div class="date"><b>JUNE</b><span>20</span></div>
    <h4>Lorem ipsum dolor sit amet consectetur</h4>
    <div class="meta"><svg style="color:var(--red)"><use href="#user"/></svg>JOHN DOE <svg style="color:var(--red);margin-left:36px"><use href="#pin"/></svg>Lorem Ipsum Dolor , USA</div>
    <p>Sed ut perspiciatis unde omnis iste natus error sivoluptatem accusantium doloremque laudantium.</p>
  </div>
  <div class="event" style="top:3253px">
    <div class="date"><b>JUNE</b><span>20</span></div>
    <h4>Lorem ipsum dolor sit amet consectetur</h4>
    <div class="meta"><svg style="color:var(--red)"><use href="#user"/></svg>JOHN DOE <svg style="color:var(--red);margin-left:36px"><use href="#pin"/></svg>Lorem Ipsum Dolor , USA</div>
    <p>Sed ut perspiciatis unde omnis iste natus error sivoluptatem accusantium doloremque laudantium.</p>
  </div>
</section>

<!-- Footer -->
<footer class="footer">
  <div class="brand"><i></i>Velmo</div>
  <div class="fcol" style="left:378px">
    <h5>Quick Links</h5>
    <ul>
      <li><svg><use href="#chev"/></svg>Home</li>
      <li><svg><use href="#chev"/></svg>About Us</li>
      <li><svg><use href="#chev"/></svg>Bar</li>
      <li><svg><use href="#chev"/></svg>Restaurant Menus</li>
      <li><svg><use href="#chev"/></svg>Event</li>
      <li><svg><use href="#chev"/></svg>Contact Us</li>
    </ul>
  </div>
  <div class="fcol" style="left:626px">
    <h5>Contact Us</h5>
    <div class="contact-item"><svg><use href="#pin"/></svg><div><small>Location</small><span>855 Lorem ipsum dolor sit<br>consectetur adipiscing elit,</span></div></div>
    <div class="contact-item"><svg><use href="#phone"/></svg><div><small>Phone</small><span>+1 555 010 2040</span></div></div>
    <div class="contact-item"><svg><use href="#mail"/></svg><div><small>Email</small><span>info@velmo.com</span></div></div>
  </div>
  <div class="fcol" style="left:904px">
    <h5>Opening Hours</h5>
    <ul>
      <li><svg><use href="#chev"/></svg>Mon&nbsp; 9.00am - 7.00pm</li>
      <li><svg><use href="#chev"/></svg>Tue&nbsp;&nbsp; 9.00am - 7.00pm</li>
      <li><svg><use href="#chev"/></svg>Wed&nbsp; 9.00am - 7.00pm</li>
      <li><svg><use href="#chev"/></svg>Thu&nbsp;&nbsp; 9.00am - 7.00pm</li>
      <li><svg><use href="#chev"/></svg>Fri&nbsp;&nbsp;&nbsp;&nbsp; 9.00am - 7.00pm</li>
      <li><svg><use href="#chev"/></svg>Sat&nbsp;&nbsp; 9.00am - 7.00pm</li>
      <li><svg><use href="#chev"/></svg>Sun&nbsp; Closed</li>
    </ul>
  </div>
  <div class="frule"></div>
  <div class="copy">© 2023 Velmo.&nbsp; |&nbsp;&nbsp;&nbsp; All Rights Reserved&nbsp;&nbsp; |</div>
</footer>

</body>
</html>
```